cleaning service

we are a cleaning company,

we have a current flyer but its very dull

I have attached it, can we make it look modern, maybe add pictures and colour

```html
<!DOCTYPE html>
<html lang="en">
<head>
<meta charset="utf-8">
<title>Cleaning Services Flyer</title>
<link rel="stylesheet" href="https://fonts.googleapis.com/css2?family=Roboto+Condensed:wght@400;700&family=Roboto:wght@300;400&display=swap">
<style>
  :root {
    --red: #8e1b1e;
    --ink: #141414;
    --body: #2b2b2b;
    --cream: #fcf1df;
    --paper: #ffffff;
    --yellow: #fdcf14;
    --orange: #fbb117;
    --pill-top: #fff3d2;
    --pill-bottom: #fde3a2;
  }
  * { margin: 0; padding: 0; box-sizing: border-box; }
  html, body { width: 849px; height: 1200px; overflow: hidden; }
  body { font-family: "Roboto", Arial, sans-serif; }
  .flyer {
    position: relative;
    width: 849px; height: 1200px; overflow: hidden;
    background: linear-gradient(180deg, var(--paper) 0%, #fef8ee 30%, var(--cream) 100%);
  }
  .abs { position: absolute; }
  .brand {
    left: 85px; top: 56px;
    font-family: "Roboto Condensed", Arial, sans-serif;
    font-weight: 700; font-size: 20px; line-height: 25px; color: var(--ink);
  }
  .brand .name { color: var(--red); }
  .corner-top { right: 0; top: 0; }
  .corner-bottom { left: 0; bottom: 0; }
  .hero-art {
    left: 612px; top: 14px; width: 190px; height: 165px;
    background: linear-gradient(160deg, #f7b21c 0%, #f39a1a 100%);
    clip-path: polygon(50% 30%, 100% 62%, 50% 100%, 0 62%);
    opacity: .9;
  }
  .service-icon {
    left: 84px; top: 200px; width: 103px; height: 103px;
    border: 1.2px solid var(--red); border-radius: 50%;
    display: flex; align-items: center; justify-content: center;
  }
  .service-icon .icon-fill {
    width: 64px; height: 56px; border-radius: 10px; background: var(--red);
  }
  .faint-art {
    left: 434px; top: 246px; width: 284px; height: 266px;
    background: radial-gradient(ellipse at 50% 45%, rgba(142,27,30,.05) 0%, rgba(142,27,30,.03) 55%, rgba(142,27,30,0) 75%);
    border-radius: 40%;
  }
  .heading {
    font-family: "Roboto Condensed", Arial, sans-serif;
    font-weight: 700; font-size: 27px; line-height: 32px; color: var(--red);
  }
  .copy {
    font-weight: 300; font-size: 16.6px; line-height: 22.8px; color: var(--body);
  }
  .copy strong {
    font-family: "Roboto Condensed", Arial, sans-serif; font-weight: 700; color: var(--ink);
  }
  .price-pill {
    left: 163px; top: 782px; width: 542px; height: 66px; border-radius: 22px;
    background: linear-gradient(180deg, var(--pill-top) 0%, var(--pill-bottom) 100%);
    display: flex; align-items: center; justify-content: center; gap: 10px;
    font-family: "Roboto Condensed", Arial, sans-serif; font-weight: 700;
    font-size: 22px; color: var(--ink);
  }
  .price-pill .amount { color: var(--red); font-size: 30px; }
  .cta-bar {
    left: 383px; top: 1081px; width: 470px; height: 62px;
    border-radius: 26px 0 0 26px;
    background: linear-gradient(90deg, #fff6e2 0%, #fde6ab 70%, #fcc94d 100%);
    padding: 10px 0 0 32px;
    font-family: "Roboto Condensed", Arial, sans-serif; font-weight: 700;
  }
  .cta-bar .note { font-size: 12px; line-height: 15px; color: var(--ink); }
  .cta-bar .call { font-size: 21.5px; line-height: 27px; color: var(--red); }
</style>
</head>
<body>
<main class="flyer">
  <svg class="abs corner-top" width="240" height="160" viewBox="0 0 240 160">
    <path d="M2 0 C30 40 90 50 150 50 C200 52 215 80 220 120 C224 145 232 155 240 158 L240 0 Z" fill="var(--yellow)"/>
    <path d="M2 0 C30 40 90 50 150 50 C200 52 215 80 220 120 C224 145 232 155 240 158 L240 0 Z" fill="var(--orange)" opacity=".35"/>
  </svg>
  <svg class="abs corner-bottom" width="270" height="180" viewBox="0 0 270 180">
    <path d="M0 0 C14 10 18 40 24 70 C32 108 70 118 130 122 C200 126 245 150 270 180 L0 180 Z" fill="var(--yellow)"/>
    <path d="M0 0 C14 10 18 40 24 70 C32 108 70 118 130 122 C200 126 245 150 270 180 L0 180 Z" fill="var(--orange)" opacity=".3"/>
  </svg>

  <div class="abs brand">CLEANING SERVICES<br>by <span class="name">MARA'S NEWS</span></div>

  <div class="abs hero-art" role="img" aria-label="Illustration of a cleaner kneeling on a patterned rug, spraying a stain"></div>

  <div class="abs faint-art" role="img" aria-label="Large faint rug and soap bubbles decoration"></div>

  <div class="abs service-icon">
    <div class="icon-fill" role="img" aria-label="Rug with soap bubbles icon"></div>
  </div>

  <h2 class="abs heading" style="left:85px; top:324px;">Rug Cleaning</h2>
  <p class="abs copy" style="left:85px; top:377px; width:335px;">Mara's Cleaning services offers professional rug cleaning service at competitive prices! Book our skilled technicians and have your textile floorings impeccably cleaned in no time. We will bring the as-new look of any rug, including antique rugs, Persian rugs,</p>
  <p class="abs copy" style="left:442px; top:381px; width:340px;">area rugs and more. If you need us to deal with a nasty stain or any other accident on your rug, you can now book our emergency rug cleaning service for a same-day appointment at no extra cost!</p>

  <h2 class="abs heading" style="left:81px; top:561px;">Oven Cleaning</h2>
  <p class="abs copy" style="left:81px; top:614px; width:335px;">Mara's Cleaning services is your best choice for an oven cleaning company in London. We know all too well that cleaning your greasy oven is not your favourite pastime, so why don't you leave all that scrubbing to our expert oven cleaners? We work with</p>
  <p class="abs copy" style="left:438px; top:616px; width:340px;">the latest equipment to challenge tough kitchen cleaning tasks. When you want your home to have a spotlessly clean oven, <strong>call 07700900417</strong> and book our professional crew today!</p>

  <div class="abs price-pill"><span>From</span><span class="amount">£42</span><span>(per hour)</span></div>

  <p class="abs copy" style="left:81px; top:885px; width:335px;">Mara's Cleaning services provides professional oven cleaning in all London boroughs. You can hire us to clean the stove in your home or restaurant. We will</p>
  <p class="abs copy" style="left:438px; top:885px; width:335px;">remove the grease and burnt food from hob or the gas burners, we will clean the appliance inside and out, including the door and the racks.</p>

  <div class="abs cta-bar">
    <div class="note">Please turnover for our services and prices</div>
    <div class="call">Please call us on 07700900417 to beat any price</div>
  </div>
</main>
</body>
</html>
```